Funding your Foodie Dreams!

I need a website design for a crowdfunding site that is 100% food/beverage oriented. Artbazaar is a crowdsourcing site and my site will be a crowdfunding site. It needs to be very clean, modern, BUT easy to use with a clear path to all critical elements.

This is the current site, that I need to fit into, http://www.grantygrove.com.hosted.pledgehostnode.com

This site, http://tinmeadow.co, is PERFECT in the fact that it does not look bland or corporate in anyway and it is beautiful and effective. My site is comparable to their "Fund" section. The photo's and ease of the site is what I would love to emulate, but my site needs to be more vibrant, fun, a happy place, which can be done with colors and textures of the site. Think of food, family, local restaurants, how you feel when you are there. I would love to have that feel just from a website.

*** These sites are some sites for competitor companies and how this site needs to operate.
boostwagon.com
mealrise.com
pledgorix.com
cashtopia.com

Here are a couple sites, that I like the look of:
us.vex.com
hopquill.com
505ladlepages.com

I would like to function like a Boostwagon but would love it to NOT look like all the rest.
Updates

I wanted to share this site, I found today.  Love the ease of the site and the look at feel but would want mine to me more fun, food, not as ... serious... but just as professional.

http://tinmeadow.co

Reason: Hello I am extending the deadline as I have yet to receive any viable designs but received some today that with some work might be the ones so please send any designs through and please send changes through quickly. I AM expecting to award this project but with the limited # of designs, might cancel it and re-issue for a far less $ amount but make it guaranteed. Thank you very much for the few designs that have been submitted to date. C

Target Market(s)

Technically savy individuals that have an entrepreneurial spirit. Individuals that will be reaching out to friends and family to use this site who will NOT be as technologically advanced and needs the site to be very clear and easy to use but not childish.

Industry/Entity Type

Crowdfunding

Font styles to use
Sans Serif

Colors
f04950
9bcb3c
ffffff
f37123
6b449b
0555a3

Requirements
Must have
• This website will be done using a white-lable platform and so I need someone that understands the limitations of that type of a platform and can work within those boundaries.

Pages Required:
Start a Campaign
Browse Campaigns
What is grantygrove?
Help
Contact

Header & Footer

Links to Social Media
Chatterbook
Chirplet
Snapvane
Clipboardly
Rambloo
Nice to have
• If you can provide any coding or direction for the coding of the design in HTML, Javascript and/or CSS, these designs will have preference.

Looking for a site that will grow from only crowdfunding to include a shopping component as well as section for campaign creators to be able to get help from service providers with their campaigns maybe a blog and a forum.
Should not have
• Do NOT provide canned websites that do not meet the Must Have's. I have to use the platform format as mentioned above as I am not have a 100% custom site developed. If these sites are provided they will be eliminated immediately.

Should not resemble a corporate site in anyway.

```html
<!DOCTYPE html>
<html lang="en">
<head>
<meta charset="utf-8">
<title>grantygrove – Funding your Foodie Dreams</title>
<link href="https://fonts.googleapis.com/css2?family=Open+Sans:wght@400;600;700&display=swap" rel="stylesheet">
<style>
:root{
  --red:#c8202a;
  --red-dark:#a5161e;
  --green:#5ea526;
  --ink:#333;
  --muted:#777;
  --line:#e2e2e2;
  --page:#f4f4f4;
  --white:#fff;
}
*{box-sizing:border-box;margin:0;padding:0}
html,body{width:738px;height:1200px;overflow:hidden}
body{background:var(--page);font-family:'Open Sans',Arial,sans-serif;color:var(--ink);font-size:7px;line-height:1.35}
.page{width:738px;height:1200px;position:relative;background:var(--white)}
.wrap{width:566px;margin:0 auto;position:relative}

.site-header{height:40px}
.brand{position:absolute;left:0;top:10px;font-size:18px;font-weight:700;color:var(--red);line-height:20px}
.search{position:absolute;right:0;top:13px;width:120px;height:15px;border:1px solid #ccc;border-radius:2px;background:var(--white)}

.main-nav{height:15px;background:var(--red);display:flex;align-items:center}
.main-nav a{color:var(--white);text-decoration:none;font-size:7px;font-weight:600;padding:0 11px}
.nav-actions{margin-left:auto;display:flex;gap:3px;padding-right:3px}
.nav-actions a{background:var(--green);padding:2px 7px;font-size:6.5px;border-radius:1px}

.hero{margin-top:13px;height:216px;border-radius:3px;position:relative;overflow:hidden;
  background:linear-gradient(180deg,#d8e3ec 0%,#c9d7e2 45%,#aabd7a 80%,#7f9e3f 100%)}
.hero-arrow{position:absolute;top:96px;width:22px;height:22px;border-radius:50%;background:rgba(40,40,40,.7)}
.hero-arrow svg{display:block;margin:6px}
.hero-arrow.prev{left:8px}.hero-arrow.next{right:8px}

.section-title{font-size:9px;font-weight:600;color:var(--ink);padding-bottom:3px;border-bottom:1px solid var(--line);margin-bottom:8px}
.recent{margin-top:18px}
.popular{margin-top:18px}

.card-row{display:flex;gap:11px}
.card{width:104.8px;height:272px;border:1px solid var(--line);background:var(--white);box-shadow:0 1px 2px rgba(0,0,0,.12);position:relative}
.card-photo{height:82px;position:relative}
.card-photo span{position:absolute;left:0;right:0;bottom:0;background:rgba(0,0,0,.6);color:var(--white);font-size:5.5px;padding:2px 3px}
.card-body{padding:5px 5px 0}
.card-title{color:var(--red);font-weight:600;font-size:6px;line-height:1.3}
.card-author{color:var(--muted);font-size:5.5px;margin:2px 0 6px}
.card-text{color:var(--muted);font-size:5.5px;line-height:1.4;height:42px}
.card-stats{position:absolute;left:5px;right:5px;top:200px}
.amount{display:flex;justify-content:space-between;font-size:8px;font-weight:700;color:var(--red)}
.amount small{font-size:5.5px;color:var(--muted);font-weight:400}
.bar{height:4px;background:var(--line);margin:5px 0}
.bar i{display:block;height:100%;background:var(--green)}
.meta{display:flex;justify-content:space-between;font-size:5px;color:var(--muted);margin-top:8px}

.story{margin-top:14px}
.story-body{display:flex;gap:14px;padding:4px 0}
.story-photo{width:122px;height:76px;background:linear-gradient(180deg,#8fb4d8,#c9d8e6 60%,#9a8a6c)}
.story-quote{flex:1;position:relative;padding:6px 18px;color:var(--muted);font-size:6.5px;line-height:1.6}
.story-quote .mark{position:absolute;font-size:26px;color:#ccc;font-family:Georgia,serif;line-height:1}
.mark.open{left:0;top:0}.mark.close{right:0;bottom:-14px}

.site-footer{position:absolute;left:0;right:0;top:1000px;height:180px;background:var(--red)}
.footer-cols{display:flex;padding-top:14px}
.footer-col{width:141px;color:var(--white)}
.footer-col h4{font-size:7px;font-weight:700;margin-bottom:6px}
.footer-col li{list-style:none;font-size:5.5px;margin-bottom:4px;opacity:.9;display:flex;align-items:center;gap:4px}
.social-dot{width:10px;height:10px;border-radius:50%;background:var(--white);opacity:.85}
.copyright{position:absolute;left:0;right:0;top:1180px;height:20px;background:var(--red-dark);color:#f2c0c2;font-size:5px;text-align:center;line-height:20px}
</style>
</head>
<body>
<div class="page">
  <header class="site-header wrap">
    <div class="brand">grantygrove</div>
    <div class="search"></div>
  </header>

  <div class="wrap">
    <nav class="main-nav">
      <a href="#">Start a Campaign</a><a href="#">Browse</a><a href="#">Contact Us</a><a href="#">About Us</a><a href="#">Help</a>
      <div class="nav-actions"><a href="#">Login</a><a href="#">Create Account</a></div>
    </nav>

    <section class="hero" role="img" aria-label="Photo of happy children jumping on a grassy field">
      <div class="hero-arrow prev"><svg width="10" height="10" viewBox="0 0 10 10"><path d="M7 1L3 5l4 4" stroke="#fff" stroke-width="2" fill="none"/></svg></div>
      <div class="hero-arrow next"><svg width="10" height="10" viewBox="0 0 10 10"><path d="M3 1l4 4-4 4" stroke="#fff" stroke-width="2" fill="none"/></svg></div>
    </section>

    <section class="recent">
      <h2 class="section-title">Recent Campaign</h2>
      <div class="card-row">
        <article class="card"><div class="card-photo" role="img" aria-label="Campaign photo of people at a table" style="background:linear-gradient(#6d6f73,#a8a39a)"><span>Lorem ipsum is simply dummy</span></div><div class="card-body"><p class="card-title">Contrary to popular belief, Lorem Ipsum is not simply</p><p class="card-author">by Mara Quillon</p><p class="card-text">Help make best dessert come true tonight. Share your good food and support the kitchen project to be awesome.</p></div><div class="card-stats"><div class="amount">$7,764 <small>USD</small><small>65%</small></div><div class="bar"><i style="width:65%"></i></div><div class="meta"><span>28 Backers</span><span>1962 Days/Left</span></div></div></article>
        <article class="card"><div class="card-photo" role="img" aria-label="Campaign photo of a crowd" style="background:linear-gradient(#7a7f86,#b9b3aa)"><span>Lorem ipsum is simply dummy</span></div><div class="card-body"><p class="card-title">Contrary to popular belief, Lorem Ipsum is not simply</p><p class="card-author">by Mara Quillon</p><p class="card-text">Help make best dessert come true tonight. Share your good food and support the kitchen project to be awesome.</p></div><div class="card-stats"><div class="amount">$7,764 <small>USD</small><small>65%</small></div><div class="bar"><i style="width:65%"></i></div><div class="meta"><span>28 Backers</span><span>1962 Days/Left</span></div></div></article>
        <article class="card"><div class="card-photo" role="img" aria-label="Campaign photo of a speaker at an event" style="background:linear-gradient(#8a6a5a,#c1b3a6)"><span>Lorem ipsum is simply dummy</span></div><div class="card-body"><p class="card-title">Contrary to popular belief, Lorem Ipsum is not simply</p><p class="card-author">by Mara Quillon</p><p class="card-text">Help make best dessert come true tonight. Share your good food and support the kitchen project to be awesome.</p></div><div class="card-stats"><div class="amount">$7,764 <small>USD</small><small>65%</small></div><div class="bar"><i style="width:65%"></i></div><div class="meta"><span>28 Backers</span><span>1962 Days/Left</span></div></div></article>
        <article class="card"><div class="card-photo" role="img" aria-label="Campaign photo on a dark red backdrop" style="background:linear-gradient(#6e1820,#9a3a3f)"><span>Lorem ipsum is simply dummy</span></div><div class="card-body"><p class="card-title">Contrary to popular belief, Lorem Ipsum is not simply</p><p class="card-author">by Mara Quillon</p><p class="card-text">Help make best dessert come true tonight. Share your good food and support the kitchen project to be awesome.</p></div><div class="card-stats"><div class="amount">$7,764 <small>USD</small><small>65%</small></div><div class="bar"><i style="width:65%"></i></div><div class="meta"><span>28 Backers</span><span>1962 Days/Left</span></div></div></article>
        <article class="card"><div class="card-photo" role="img" aria-label="Campaign portrait photo" style="background:linear-gradient(#9aa6b4,#b58f78)"><span>Lorem ipsum is simply dummy</span></div><div class="card-body"><p class="card-title">Contrary to popular belief, Lorem Ipsum is not simply</p><p class="card-author">by Mara Quillon</p><p class="card-text">Help make best dessert come true tonight. Share your good food and support the kitchen project to be awesome.</p></div><div class="card-stats"><div class="amount">$7,764 <small>USD</small><small>65%</small></div><div class="bar"><i style="width:65%"></i></div><div class="meta"><span>28 Backers</span><span>1962 Days/Left</span></div></div></article>
      </div>
    </section>

    <section class="popular">
      <h2 class="section-title">Popular Campaign</h2>
      <div class="card-row">
        <article class="card"><div class="card-photo" role="img" aria-label="Campaign photo of a street scene" style="background:linear-gradient(#5a4a3e,#a27a4e)"><span>Lorem ipsum is simply dummy</span></div><div class="card-body"><p class="card-title">Contrary to popular belief, Lorem Ipsum is not simply</p><p class="card-author">by Mara Quillon</p><p class="card-text">Help make best dessert come true tonight. Share your good food and support the kitchen project to be awesome.</p></div><div class="card-stats"><div class="amount">$7,764 <small>USD</small><small>65%</small></div><div class="bar"><i style="width:65%"></i></div><div class="meta"><span>28 Backers</span><span>1962 Days/Left</span></div></div></article>
        <article class="card"><div class="card-photo" role="img" aria-label="Campaign photo with bright red colours" style="background:linear-gradient(#b0262c,#e06a3c)"><span>Lorem ipsum is simply dummy</span></div><div class="card-body"><p class="card-title">Contrary to popular belief, Lorem Ipsum is not simply</p><p class="card-author">by Mara Quillon</p><p class="card-text">Help make best dessert come true tonight. Share your good food and support the kitchen project to be awesome.</p></div><div class="card-stats"><div class="amount">$7,764 <small>USD</small><small>65%</small></div><div class="bar"><i style="width:65%"></i></div><div class="meta"><span>28 Backers</span><span>1962 Days/Left</span></div></div></article>
        <article class="card"><div class="card-photo" role="img" aria-label="Black and white campaign portrait" style="background:linear-gradient(#2e2e2e,#8a8a8a)"><span>Lorem ipsum is simply dummy</span></div><div class="card-body"><p class="card-title">Contrary to popular belief, Lorem Ipsum is not simply</p><p class="card-author">by Mara Quillon</p><p class="card-text">Help make best dessert come true tonight. Share your good food and support the kitchen project to be awesome.</p></div><div class="card-stats"><div class="amount">$7,764 <small>USD</small><small>65%</small></div><div class="bar"><i style="width:65%"></i></div><div class="meta"><span>28 Backers</span><span>1962 Days/Left</span></div></div></article>
        <article class="card"><div class="card-photo" role="img" aria-label="Campaign photo of a tall ship at sea" style="background:linear-gradient(#9fbcd8,#5b7f9e)"><span>Lorem ipsum is simply dummy</span></div><div class="card-body"><p class="card-title">Contrary to popular belief, Lorem Ipsum is not simply</p><p class="card-author">by Mara Quillon</p><p class="card-text">Help make best dessert come true tonight. Share your good food and support the kitchen project to be awesome.</p></div><div class="card-stats"><div class="amount">$7,764 <small>USD</small><small>65%</small></div><div class="bar"><i style="width:65%"></i></div><div class="meta"><span>28 Backers</span><span>1962 Days/Left</span></div></div></article>
        <article class="card"><div class="card-photo" role="img" aria-label="Campaign photo of a group of people" style="background:linear-gradient(#5c5f66,#9a948c)"><span>Lorem ipsum is simply dummy</span></div><div class="card-body"><p class="card-title">Contrary to popular belief, Lorem Ipsum is not simply</p><p class="card-author">by Mara Quillon</p><p class="card-text">Help make best dessert come true tonight. Share your good food and support the kitchen project to be awesome.</p></div><div class="card-stats"><div class="amount">$7,764 <small>USD</small><small>65%</small></div><div class="bar"><i style="width:65%"></i></div><div class="meta"><span>28 Backers</span><span>1962 Days/Left</span></div></div></article>
      </div>
    </section>

    <section class="story">
      <h2 class="section-title">Featured Success Story</h2>
      <div class="story-body">
        <div class="story-photo" role="img" aria-label="Photo of a man celebrating under a blue sky"></div>
        <blockquote class="story-quote">
          <span class="mark open">&ldquo;</span>
          Contrary to popular belief, Lorem Ipsum is not simply random text. It has roots in a piece of classical Latin literature from 45 BC, making it over 2000 years old. Rowan Tellwick, a Latin professor at Ashgrove College in Virginia, looked up one of the more obscure Latin words, consectetur.
          <span class="mark close">&rdquo;</span>
        </blockquote>
      </div>
    </section>
  </div>

  <footer class="site-footer">
    <div class="wrap footer-cols">
      <div class="footer-col"><h4>Browse Campaigns</h4><ul><li>Featured Campaigns</li><li>Successful Campaigns</li><li>New Campaigns</li><li>Ending Soon</li><li>Most Funded Campaigns</li></ul></div>
      <div class="footer-col"><h4>About</h4><ul><li>About grantygrove</li><li>Contact Us</li><li>Help</li><li>Privacy Policy</li><li>Terms Of Service</li></ul></div>
      <div class="footer-col"><h4>Follow Us</h4><ul><li><span class="social-dot"></span>Follow us on Chatterbook</li><li><span class="social-dot"></span>Follow us on Chirplet</li><li><span class="social-dot"></span>RSS Feed</li></ul></div>
      <div class="footer-col"><h4>Contact Us</h4><ul><li>Address: 12 Orchard Lane,</li><li>Millbrook, NY 10000</li><li>Ph No.: 555-0148-200</li><li>E-mail: info@grantygrove.com</li></ul></div>
    </div>
  </footer>
  <div class="copyright">Copyright &copy; grantygrove. All Rights Reserved.</div>
</div>
</body>
</html>
```